Wood Fired Pizza business needs a business card design

We need a business car design for a new company based in Texas called "Brindle Fern" a play off of Thorny Elm. We hand craft pizzas and cook them in our wood fired oven at temp. that reach 900 degrease, allowing the pizza to cook in 90 sec. Our customer base is private catering, festivals, and farmers markets. We would like to see designs that follow the Thorny Elm brand of Camoflauge, and Orange text. The final design should communicate pizza cooked in a wood fired oven.

Industry/Entity Type

Business

```html
<!DOCTYPE html>
<html lang="en">
<head>
<meta charset="utf-8">
<title>Brindle Fern – Business Card</title>
<link href="https://fonts.googleapis.com/css2?family=Lato:wght@400;700;900&display=swap" rel="stylesheet">
<style>
  :root {
    --backdrop: #e9e4dd;
    --wood-dark: #2e2019;
    --wood-mid: #3d2b21;
    --wood-light: #4a3528;
    --paper: #f4f2ec;
    --orange: #f0671c;
    --ink: #161616;
  }
  * { box-sizing: border-box; margin: 0; padding: 0; }
  html, body {
    width: 1200px; height: 900px; overflow: hidden;
    background: var(--backdrop);
    font-family: "Lato", Arial, sans-serif;
  }
  .stage {
    width: 1200px; height: 900px;
    display: flex; flex-direction: column; align-items: center; justify-content: center;
    gap: 40px;
  }
  .card {
    position: relative;
    width: 630px; height: 360px;
    overflow: hidden;
    box-shadow: 0 10px 28px rgba(0,0,0,0.25);
  }
  .wood {
    position: absolute; inset: 0;
    background: linear-gradient(100deg, var(--wood-dark) 0%, var(--wood-light) 45%, var(--wood-mid) 70%, var(--wood-dark) 100%);
  }
  .wordmark {
    color: var(--orange);
    font-weight: 900;
    line-height: 1;
    letter-spacing: 0.01em;
    text-transform: uppercase;
  }
  .tagline {
    color: var(--orange);
    font-weight: 400;
    text-transform: uppercase;
    letter-spacing: 0.42em;
  }
  /* front */
  .card-front .brand {
    position: absolute; inset: 0;
    display: flex; flex-direction: column; align-items: center; justify-content: center;
  }
  .card-front .wordmark { font-size: 62px; }
  .card-front .tagline { font-size: 19px; margin-top: 6px; }
  /* back */
  .paper-band {
    position: absolute; left: 0; right: 0; top: 78px; height: 190px;
    background: var(--paper);
    display: flex; align-items: center; justify-content: space-between;
    padding: 0 40px 0 44px;
  }
  .card-back .brand { display: flex; flex-direction: column; margin-top: 48px; }
  .card-back .wordmark { font-size: 46px; }
  .card-back .tagline { font-size: 15px; margin-top: 4px; }
  .contact { align-self: flex-start; margin-top: 26px; }
  .contact-name { color: var(--orange); font-weight: 700; font-size: 21px; }
  .contact-role { color: var(--ink); font-weight: 700; font-size: 15px; margin-top: 2px; }
  .contact-list { list-style: none; margin-top: 20px; }
  .contact-list li {
    display: flex; align-items: center; gap: 8px;
    color: var(--ink); font-size: 16px; line-height: 1.4;
  }
  .contact-list svg { width: 14px; height: 14px; fill: var(--orange); }
  .address {
    position: absolute; left: 0; right: 0; bottom: 38px;
    text-align: center; color: var(--orange); font-size: 17px;
  }
</style>
</head>
<body>
<main class="stage">
  <section class="card card-front">
    <div class="wood" role="img" aria-label="Dark oak wood grain surface"></div>
    <div class="brand">
      <div class="wordmark">Brindle Fern</div>
      <div class="tagline">Hand Craft Pizzas</div>
    </div>
  </section>

  <section class="card card-back">
    <div class="wood" role="img" aria-label="Dark oak wood grain surface"></div>
    <div class="paper-band">
      <div class="brand">
        <div class="wordmark">Brindle Fern</div>
        <div class="tagline">Hand Craft Pizzas</div>
      </div>
      <div class="contact">
        <div class="contact-name">Dana Wells</div>
        <div class="contact-role">Manager</div>
        <ul class="contact-list">
          <li>
            <svg viewBox="0 0 24 24" aria-hidden="true"><path d="M6.6 10.8a15.1 15.1 0 0 0 6.6 6.6l2.2-2.2a1 1 0 0 1 1-.25 11.4 11.4 0 0 0 3.6.57 1 1 0 0 1 1 1V20a1 1 0 0 1-1 1A17 17 0 0 1 3 4a1 1 0 0 1 1-1h3.5a1 1 0 0 1 1 1c0 1.25.2 2.45.57 3.57a1 1 0 0 1-.25 1z"/></svg>
            +1 512 555 0148
          </li>
          <li>
            <svg viewBox="0 0 24 24" aria-hidden="true"><path d="M2 5h20v14H2z M3.5 6.5 12 13l8.5-6.5" fill="var(--orange)"/><path d="M3.5 6.5 12 13l8.5-6.5" fill="none" stroke="#fff" stroke-width="1.6"/></svg>
            dwells@brindlefern.com
          </li>
        </ul>
      </div>
    </div>
    <p class="address">Unit No : 4, Cedar Lane No. 7, Hill Town, TX 78610</p>
  </section>
</main>
</body>
</html>
```